Website for Community Storage Startup Company

We're looking for a great design that looks good on mobile devices (as well as the web) - Layout should be responsive and able to scale to many sized devices.

It should provide a good user-experience for people browsing the site with heavy focus on search and search results pages - It should be extremely easy to search, see results and add your own information.

Search parameters should be Location (Text), Dates (Calendar pop up), Price (slider) with optional extra parameters to be displayed (You can just call them Parameter1, Parameter2 etc. for Examples- we'd like to see options of no extra parameters and up to 4 others)

Please include a favicon for the site - we've provided the logo we had designed.

Pages We Must Have:

1) Home Page
2) Search Page (most likely map based)
3) Search Results Page (most likely map based) - we want the search options/results to slide in and out as appropriate - please visualize
Information Page - this is branded and would present information for many possible pages like Terms & Conditions or a FAQ page etc.
4) My Account Page - Should be an inline editable page with Name/Address/Financial information etc. showing
5) Sign-up Page - This could be a slide in element on another page or part of the account page, or separate as you think works best

Ideally this would all work like a single page app with a common theme but we're interested to see your ideas of tying pages together or keeping them separate while fitting our brief.

Examples of things we like;

a) roomvale - mobile and web based layouts - we like the map on the side and data input on the other side
b) http://www.qorvent.example/qv/airlines/ - scroll down slightly to the first video - about 0:28 in we like the map on the side and the panel on the side with details you can refine etc. All over we like the site presented through the video

Nice to Have:
- The ability to provide the finished design as sliced CSS, HTML and JS
Updates

Project Deadline Extended
Reason: Feedback has suggested that the timeline is too tight, we've extended it but are very interested in seeing initial page designs sooner rather than later to provide feedback. Thanks!

Thanks for your contributions so far :)  We've come to realize that in general we're preferring darker color schemes - if you're pulling colors from our logo try to stick to the text colors :)

We like narrow headers and footers and a map based interface. Sliders for information are good and we'd like to see how checkbox elements would play out too.

Examples of how information may pop up from markers would be nice too.

Thanks for everything so far!

Target Market(s)

Young to middle aged adults in the USA

Industry/Entity Type

Airlines

Font styles to use
Sans Serif

Colors

Designer to choose colors to be used in the design.

Requirements
Must have
• 1) Home Page
Nice to have
• The ability to provide the finished design as sliced CSS, HTML and JS

We think a map with markers should figure heavily in search results and searching.

```html
<!DOCTYPE html>
<html lang="en">
<head>
<meta charset="utf-8">
<title>Stowly – Community Storage</title>
<link href="https://fonts.googleapis.com/css2?family=Open+Sans:wght@400;600&family=Raleway:wght@300&display=swap" rel="stylesheet">
<style>
:root{
  --green:#9cb642;
  --green-dark:#6d8a1e;
  --navy:#06305c;
  --navy-deep:#0a2440;
  --charcoal:#1d1d1d;
  --bar:#262626;
  --ink:#222;
  --muted:#666;
  --footer-text:#8a8a8a;
  --teal:#8cc0d4;
  --grey-btn:#c3c6c8;
  --field-bg:#f7fae6;
}
*{box-sizing:border-box;margin:0;padding:0}
html,body{width:960px;height:1200px;overflow:hidden;background:#fff}
body{position:relative;font-family:"Open Sans",Arial,sans-serif;color:var(--ink)}
.abs{position:absolute}

/* header */
.header{left:0;top:0;width:960px;height:77px;background:#fff}
.brand{left:80px;top:14px;display:flex;align-items:center;gap:8px}
.brand-mark{width:22px;height:22px;border-radius:50%;background:var(--teal)}
.brand-name{font-size:24px;font-weight:400;color:#2a3540;letter-spacing:.5px}
.btn-register,.btn-login{top:18px;height:17px;width:65px;color:#fff;font-size:10px;text-align:center;line-height:17px}
.btn-register{left:742px;background:var(--grey-btn)}
.btn-login{left:814px;background:var(--teal)}
.top-search{left:673px;top:42px;width:207px;height:17px;border:1px solid #d5d5d5;font-size:9.5px;color:#777;line-height:15px;padding-left:7px}
.top-search-btn{right:-1px;top:-1px;width:23px;height:17px;background:var(--green);display:flex;align-items:center;justify-content:center}

/* hero */
.hero{left:0;top:77px;width:960px;height:405px;background:linear-gradient(90deg,#9a7a62 0%,#c9b7a6 25%,#d9d6d2 45%,#bfa690 65%,#cfc6bb 85%,#a9998a 100%)}
.hero-arrow{top:258px;width:38px;height:38px;border:2px solid #fff;border-radius:50%;display:flex;align-items:center;justify-content:center}
.search-bar{left:126px;top:261px;width:701px;height:44px;background:rgba(40,40,40,.85)}
.field{top:5px;height:34px;background:#fff;font-size:10px;color:#333;line-height:34px;padding-left:8px}
.field svg{position:absolute;top:9px}
.slider-track{left:50px;top:15px;width:118px;height:6px;border-radius:3px;background:#ddd}
.slider-fill{left:0;top:0;width:45px;height:6px;border-radius:3px;background:var(--green-dark)}
.slider-knob{left:42px;top:-4px;width:6px;height:14px;border-radius:2px;background:#5e6e3a}
.price-tip{left:448px;top:244px;width:56px;height:17px;background:#fff;font-size:9.5px;text-align:center;line-height:17px;color:#333}
.price-tip::after{content:"";position:absolute;left:14px;bottom:-4px;border:4px solid transparent;border-bottom:0;border-top-color:#fff}
.search-btn{left:611px;top:5px;width:85px;height:34px;background:var(--green);color:#fff;font-weight:600;font-size:13px;text-align:center;line-height:34px}

/* features */
.card-img{top:550px;width:239px;height:104px}
.card-title{width:239px;text-align:center;font-size:12.5px;color:#111;letter-spacing:.2px}
.card-text{width:239px;text-align:center;font-size:10px;line-height:15px;color:var(--muted)}
.card-text.justify{text-align:justify;text-align-last:center}
.read-more{left:163px;top:753px;width:99px;height:23px;border-radius:12px;background:var(--green);color:#3c4a12;font-size:9.5px;text-align:center;line-height:23px}
.eye{left:105px;top:35px;width:32px;height:32px;border-radius:50%;background:var(--green);display:flex;align-items:center;justify-content:center}
.fold{right:0;top:0;width:0;height:0;border-left:14px solid #e8e8e8;border-bottom:14px solid transparent}

/* contact band */
.band{left:0;top:843px;width:960px;height:56px;background:var(--navy)}
.band-text{left:81px;top:13px;color:#fff;font-size:14px;line-height:15px}
.band-input{top:18px;width:115px;height:21px;background:var(--field-bg);font-size:11px;color:#888;line-height:21px;padding-left:8px}
.band-btn{left:765px;top:18px;width:114px;height:21px;background:var(--navy-deep);color:#8ea3bb;font-size:11px;text-align:center;line-height:21px}
.band-pointer{left:858px;top:56px;border:5px solid transparent;border-bottom:0;border-top-color:var(--navy)}

/* footer */
.footer{left:0;top:899px;width:960px;height:257px;background:var(--charcoal)}
.col-title{top:36px;font-family:"Raleway",sans-serif;font-weight:300;font-size:26px;color:#fff}
.col-list{list-style:none;font-size:10.5px;line-height:14.4px;color:var(--footer-text);white-space:nowrap}
.col-list .light{color:#ddd}
.bottom-bar{left:0;top:1156px;width:960px;height:44px;background:var(--bar)}
.socials{left:80px;top:0;width:236px;height:44px;background:#2c2c2c;display:flex}
.social{width:45.6px;height:44px;display:flex;align-items:center;justify-content:center}
.social.active{background:var(--navy)}
.social span{width:19px;height:19px;border-radius:50%;background:#5a5a5a}
.social.active span{background:#fff}
.legal{right:78px;top:15px;font-size:10px;color:#fff}
.legal a{color:#fff;text-decoration:none}
.legal .sep{margin:0 5px}
.version{left:936px;top:16px;font-size:9.5px;color:#fff}
</style>
</head>
<body>

<header class="header abs">
  <div class="brand abs"><span class="brand-mark"></span><span class="brand-name">Stowly</span></div>
  <div class="btn-register abs">Register</div>
  <div class="btn-login abs">Login</div>
  <div class="top-search abs">Chennai, Tamilnadu
    <div class="top-search-btn abs"><svg width="9" height="9" viewBox="0 0 10 10"><circle cx="4" cy="4" r="3" fill="none" stroke="#fff" stroke-width="1.4"/><line x1="6.2" y1="6.2" x2="9" y2="9" stroke="#fff" stroke-width="1.4"/></svg></div>
  </div>
</header>

<section class="hero abs" role="img" aria-label="Warehouse manager standing in front of blurred storage shelving"></section>

<div class="hero-arrow abs" style="left:30px"><svg width="10" height="16" viewBox="0 0 10 16"><polyline points="8,1 2,8 8,15" fill="none" stroke="#fff" stroke-width="1.6"/></svg></div>
<div class="hero-arrow abs" style="left:887px"><svg width="10" height="16" viewBox="0 0 10 16"><polyline points="2,1 8,8 2,15" fill="none" stroke="#fff" stroke-width="1.6"/></svg></div>

<div class="price-tip abs">$382.30</div>
<form class="search-bar abs">
  <div class="field abs" style="left:5px;width:143px">Location
    <svg style="left:123px" width="11" height="15" viewBox="0 0 11 15"><path d="M5.5 0a5.5 5.5 0 0 1 5.5 5.5C11 9.5 5.5 15 5.5 15S0 9.5 0 5.5A5.5 5.5 0 0 1 5.5 0z" fill="#8a8a8a"/><circle cx="5.5" cy="5.5" r="2" fill="#fff"/></svg>
  </div>
  <div class="field abs" style="left:153px;width:85px">Dates
    <svg style="left:62px" width="15" height="15" viewBox="0 0 15 15"><rect x=".5" y="1.5" width="14" height="13" fill="none" stroke="#999"/><rect x=".5" y="1.5" width="14" height="3" fill="#999"/><g fill="#999"><rect x="3" y="6" width="2" height="2"/><rect x="6.5" y="6" width="2" height="2"/><rect x="10" y="6" width="2" height="2"/><rect x="3" y="10" width="2" height="2"/><rect x="6.5" y="10" width="2" height="2"/><rect x="10" y="10" width="2" height="2"/></g></svg>
  </div>
  <div class="field abs" style="left:244px;width:180px">Price
    <div class="slider-track abs"><div class="slider-fill abs"></div><div class="slider-knob abs"></div></div>
  </div>
  <div class="field abs" style="left:430px;width:85px">Parameter 1</div>
  <div class="field abs" style="left:520px;width:85px">Parameter 2</div>
  <div class="search-btn abs">Search</div>
</form>

<article>
  <div class="card-img abs" style="left:81px;background:linear-gradient(180deg,#6b5132,#b9874a 55%,#c8a36c)" role="img" aria-label="Warehouse aisle with stacked pallets of goods">
    <div class="fold abs"></div>
    <div class="eye abs"><svg width="16" height="10" viewBox="0 0 16 10"><path d="M0 5Q8-3 16 5Q8 13 0 5z" fill="#fff"/><circle cx="8" cy="5" r="2.3" fill="#9cb642"/></svg></div>
  </div>
  <h3 class="card-title abs" style="left:81px;top:669px;font-weight:400">PESTRIES</h3>
  <p class="card-text justify abs" style="left:81px;top:692px">Shop elegant tapesrries sit amet, consectetuer adipiscing elit, sed diam nonummy nibh.Sed ut perspiciatis unde omnis</p>
  <div class="read-more abs">READ MORE</div>
</article>

<article>
  <div class="card-img abs" style="left:362px;background:linear-gradient(180deg,#3a4a5c,#b89a6e 45%,#c9aa7a)" role="img" aria-label="Warehouse hall filled with wooden crates"></div>
  <h3 class="card-title abs" style="left:362px;top:671px;font-weight:400">LOREM IPSUM DOLOR SIT AME</h3>
  <p class="card-text abs" style="left:362px;top:693px">Lorem ipsum dolor sit amet, consectetuer adipicing elit, sed diam nonummy nibh.Sed ut perspiciatis unde omnis</p>
</article>

<article>
  <div class="card-img abs" style="left:642px;background:linear-gradient(180deg,#8c9a70,#a6ad86 50%,#6e5a44)" role="img" aria-label="Living room with a cream sofa and green walls"></div>
  <h3 class="card-title abs" style="left:642px;top:673px;font-weight:400">ADIPISCING ELIT</h3>
  <p class="card-text justify abs" style="left:642px;top:695px">Dolor sit amet, consectetuer adipicing elit, sed diam nonummy nibh.Sed ut perspiciatis unde omnis iste natus error<br>sit voluptatem</p>
</article>

<section class="band abs">
  <p class="band-text abs">Nunc dolor nibh, volutpat at molestie ut, luctus<br>ac leo. Sed fermentum quam turpis</p>
  <div class="band-input abs" style="left:507px">Name</div>
  <div class="band-input abs" style="left:636px">Email</div>
  <div class="band-btn abs">Contact us</div>
  <div class="band-pointer abs"></div>
</section>

<footer class="footer abs">
  <h4 class="col-title abs" style="left:82px">Navigatie</h4>
  <ul class="col-list abs" style="left:82px;top:89px">
    <li>Home</li><li>werknemers</li><li>gepensioneerden</li><li>ex-werknemers</li><li>pensioenwoordenboek</li><li>faq</li><li>over Larkwell Pensioen</li>
  </ul>
  <h4 class="col-title abs" style="left:250px">Interessante links</h4>
  <ul class="col-list abs" style="left:251px;top:91px">
    <li>Landelijk Rentenoverzicht</li><li>RBK</li><li>ZVA</li>
  </ul>
  <h4 class="col-title abs" style="left:498px">Contact</h4>
  <ul class="col-list abs" style="left:501px;top:90px">
    <li>Larkwell Pensioen</li><li>Contactgegevens</li><li>0900 - 4821</li><li>info@larkwell.example</li>
  </ul>
  <h4 class="col-title abs" style="left:716px">Nieuws</h4>
  <ul class="col-list abs" style="left:716px;top:90px">
    <li>Viking - Premium Verdant Template</li><li>http://lnk.ex/Qx7R2m #tplhub</li><li class="light">about 9 hours ago</li>
  </ul>
  <ul class="col-list abs" style="left:716px;top:149px">
    <li>Modus - Premium Verdant Template</li><li>http://lnk.ex/Qx7R2m #tplhub</li><li class="light">about 12 hours ago</li>
  </ul>
</footer>

<div class="bottom-bar abs">
  <div class="socials abs">
    <div class="social active"><span></span></div>
    <div class="social"><span></span></div>
    <div class="social"><span></span></div>
    <div class="social"><span></span></div>
    <div class="social"><span></span></div>
  </div>
  <p class="legal abs">Copyright © yourwebsite<span class="sep">|</span><a>Terms &amp; Conditions</a><span class="sep">|</span><a>Privacy Policy</a><span class="sep">|</span><a>Cookies Policy</a><span class="sep">|</span><a>Contact us</a></p>
  <span class="version abs">M3</span>
</div>

</body>
</html>
```